Business Card Design Project

Looking for a business card that our customers will remember. We are a high end Travel Agency.
Need a re-memorable classy business card.
Both sides full color.
Must have the following details.
Voyage Harbor Logo (see attached)
4B Wattle Lane
Penhurst Sydney NSW 2241
Phone: 02 9471 3652
Fax: 02 9563 4417
sales@voyageharbor-example.com.au
Consultant Name
Anything else you think we need

```html
<!DOCTYPE html>
<html lang="en">
<head>
<meta charset="utf-8">
<title>Voyage Harbor – Business Card</title>
<link rel="stylesheet" href="https://fonts.googleapis.com/css2?family=Source+Sans+3:wght@400;600&display=swap">
<style>
  :root {
    --backdrop: #2b2b2b;
    --sun: #ffcc00;
    --paper: #ffffff;
    --harbor-blue: #2b5e88;
    --ink: #1e1e1e;
    --shadow: rgba(0, 0, 0, 0.45);
  }
  * { margin: 0; padding: 0; box-sizing: border-box; }
  html, body {
    width: 1200px;
    height: 900px;
    overflow: hidden;
    background: var(--backdrop);
    font-family: "Source Sans 3", sans-serif;
  }
  .stage {
    position: relative;
    width: 1200px;
    height: 900px;
  }
  .card {
    position: absolute;
    top: 303px;
    width: 530px;
    height: 294px;
    border-radius: 18px;
    overflow: hidden;
    box-shadow: 0 4px 10px var(--shadow);
  }
  .card--front {
    left: 54px;
    background: var(--sun);
  }
  .card--back {
    left: 615px;
    background: var(--paper);
  }
  .wordmark {
    position: absolute;
    color: var(--harbor-blue);
    font-weight: 400;
    white-space: nowrap;
    line-height: 1;
  }
  .card--front .wordmark {
    left: 0;
    right: 0;
    top: 124px;
    text-align: center;
    font-size: 34px;
    letter-spacing: 1px;
  }
  .card--back .wordmark {
    left: 42px;
    top: 28px;
    font-size: 38px;
    letter-spacing: 1px;
  }
  .website {
    position: absolute;
    left: 44px;
    top: 72px;
    font-size: 12.5px;
    color: var(--ink);
  }
  .consultant {
    position: absolute;
    left: 44px;
    top: 124px;
  }
  .consultant__name {
    font-size: 22px;
    color: var(--harbor-blue);
    letter-spacing: 0.3px;
    line-height: 1.1;
  }
  .consultant__role {
    font-size: 15px;
    color: var(--ink);
    margin-top: 4px;
  }
  .band {
    position: absolute;
    left: 0;
    top: 0;
    width: 530px;
    height: 294px;
  }
  .address {
    position: absolute;
    left: 42px;
    top: 232px;
    font-size: 14px;
    line-height: 17px;
    color: var(--ink);
    display: flex;
    gap: 5px;
  }
  .address svg { margin-top: 1px; flex: none; }
  .contact-list {
    position: absolute;
    right: 22px;
    top: 214px;
    list-style: none;
    font-size: 14px;
    line-height: 18px;
    color: var(--ink);
    text-align: right;
  }
  .contact-list li {
    display: flex;
    justify-content: flex-end;
    align-items: center;
    gap: 7px;
  }
  .contact-list svg { flex: none; }
</style>
</head>
<body>
<main class="stage">

  <section class="card card--front" aria-label="Card front">
    <div class="wordmark">Voyage Harbor</div>
  </section>

  <section class="card card--back" aria-label="Card back">
    <svg class="band" viewBox="0 0 530 294" aria-hidden="true">
      <path d="M0,180 Q270,218 530,122 L530,294 L0,294 Z" fill="var(--sun)"/>
      <path d="M0,193 Q270,232 530,134 Q280,244 0,207 Z" fill="var(--paper)"/>
    </svg>

    <div class="wordmark">Voyage Harbor</div>
    <div class="website">www.voyageharbor-example.com.au</div>

    <div class="consultant">
      <div class="consultant__name">DANIEL WHITFORD</div>
      <div class="consultant__role">Travel Consultant</div>
    </div>

    <div class="address">
      <svg width="12" height="16" viewBox="0 0 12 16" aria-hidden="true">
        <path d="M6,0 C2.7,0 0,2.6 0,5.9 C0,10 6,16 6,16 C6,16 12,10 12,5.9 C12,2.6 9.3,0 6,0 Z" fill="var(--paper)"/>
        <circle cx="6" cy="6" r="2.2" fill="var(--sun)"/>
      </svg>
      <div>4B Wattle Lane<br>Penhurst Sydney NSW 2241</div>
    </div>

    <ul class="contact-list">
      <li>02 9471 3652
        <svg width="11" height="11" viewBox="0 0 11 11" aria-hidden="true">
          <circle cx="5.5" cy="5.5" r="5.5" fill="var(--paper)"/>
          <path d="M3.4,2.6 L4.6,2.6 L5,4 L4.3,4.6 Q5,6.1 6.4,6.8 L7,6.1 L8.4,6.5 L8.4,7.7 Q5.6,8 3.4,2.6 Z" fill="var(--sun)"/>
        </svg>
      </li>
      <li>02 9563 4417
        <svg width="11" height="11" viewBox="0 0 11 11" aria-hidden="true">
          <rect x="2.5" y="0.5" width="6" height="3.5" fill="var(--paper)"/>
          <rect x="0.5" y="4.5" width="10" height="6" rx="1.5" fill="var(--paper)"/>
        </svg>
      </li>
      <li>sales@voyageharbor-example.com.au
        <svg width="11" height="8" viewBox="0 0 11 8" aria-hidden="true">
          <rect x="0" y="0" width="11" height="8" rx="1" fill="var(--paper)"/>
          <path d="M0.5,0.8 L5.5,4.6 L10.5,0.8" fill="none" stroke="var(--sun)" stroke-width="1"/>
        </svg>
      </li>
    </ul>
  </section>

</main>
</body>
</html>
```